Benefits of introducing UV light into HVAC systems

UV light is an effective way of reducing bacteria and viruses within offices and homes using a ventilation and/or air conditioning system. Clearly show the benefits in an infographic that an air conditioning company could place on their website to educate and persuade potential customers.

Target Market(s)

Commercial and domestic

```html
<!DOCTYPE html>
<html lang="en">
<head>
<meta charset="utf-8">
<title>4 Benefits of HVAC UV Lights – Coolcrest Air</title>
<link href="https://fonts.googleapis.com/css2?family=Poppins:wght@300;400;500;600;700;800&family=Oswald:wght@500;600&display=swap" rel="stylesheet">
<style>
:root{
  --blue:#2f86c6;
  --blue-dark:#134b7f;
  --blue-deep:#1f6aa8;
  --red:#c73a42;
  --red-dark:#a11f26;
  --paper:#f5f5f5;
  --card-inner:#ebebeb;
  --ink:#222;
  --white:#fff;
}
*{box-sizing:border-box;margin:0;padding:0}
html,body{width:1052px;height:1200px;overflow:hidden;background:#888}
body{font-family:'Poppins',sans-serif;color:var(--ink)}
.sheet{position:relative;width:1052px;height:1200px;background:var(--paper);overflow:hidden}

.brand{position:absolute;top:58px;left:0;width:100%;display:flex;justify-content:center;align-items:center;gap:16px}
.brand-dot{width:58px;height:58px;border-radius:50%;background:var(--blue)}
.brand-name{font-weight:700;font-size:42px;letter-spacing:6px;color:var(--blue);text-transform:uppercase}

.intro-band{position:absolute;left:0;top:217px;width:100%;height:186px;background:var(--red)}
.title-banner{position:absolute;left:63px;top:167px;width:926px;height:100px}
.title-banner h1{position:absolute;inset:0;display:flex;align-items:center;justify-content:center;color:var(--white);font-weight:700;font-size:32px;letter-spacing:.2px}
.intro-text{position:absolute;left:26px;top:300px;width:1000px;text-align:center;color:var(--white);font-size:17px;line-height:20.5px}

.benefits-badge{position:absolute;left:364px;top:427px;width:324px;height:72px}
.benefits-badge span{position:absolute;left:12px;top:0;width:298px;height:61px;display:flex;align-items:center;justify-content:center;color:var(--white);font-weight:700;font-size:40px}

.timeline{position:absolute;left:27px;top:531px;width:997px;height:2px;background:#222}
.step{position:absolute;top:513px;width:40px;height:40px;border-radius:50%;border:3px solid var(--white);display:flex;align-items:center;justify-content:center;color:var(--white);font-family:'Oswald',sans-serif;font-weight:500;font-size:22px;box-shadow:0 1px 3px rgba(0,0,0,.25)}
.connector{position:absolute;top:553px;width:2px;height:43px}

.card{position:absolute;top:621px;width:222px;height:332px;background:var(--white);padding:6px;box-shadow:0 2px 6px rgba(0,0,0,.25)}
.card-inner{width:100%;height:100%;background:var(--card-inner);padding:62px 9px 0 10px}
.card-tab{position:absolute;left:-13px;top:-25px;width:154px;height:84px}
.card-num{position:absolute;left:12px;top:-7px;width:56px;height:56px;border-radius:50%;background:var(--white);display:flex;align-items:center;justify-content:center}
.card-num span{width:50px;height:50px;border-radius:50%;border:2px solid currentColor;display:flex;align-items:center;justify-content:center;font-family:'Oswald',sans-serif;font-weight:600;font-size:34px}
.card-foot{position:absolute;left:11px;bottom:-13px;width:188px;height:11px;clip-path:polygon(0 0,100% 0,94% 100%,6% 100%)}
.card-icon{display:block;width:34px;height:48px;margin:0 auto 8px;border-radius:6px}
.card-icon.square{width:58px;height:58px;border-radius:14px;margin-bottom:2px}
.card h2{font-size:12.3px;font-weight:600;text-align:center;text-transform:uppercase;margin-bottom:5px;white-space:nowrap}
.card ul{list-style:none}
.card li{position:relative;padding-left:14px;font-size:9.5px;line-height:11.4px;text-align:justify;margin-bottom:11px;color:#333}
.card li svg{position:absolute;left:0;top:1px;width:9px;height:9px}

.is-blue{color:var(--blue)} .bg-blue{background:var(--blue)}
.is-navy{color:var(--blue-dark)} .bg-navy{background:var(--blue-dark)}
.is-red{color:var(--red)} .bg-red{background:var(--red)}
.is-crimson{color:var(--red-dark)} .bg-crimson{background:var(--red-dark)}

.closing{position:absolute;left:27px;top:1007px;width:998px;font-size:17.6px;line-height:21.5px;text-align:justify;text-align-last:center;color:#222}

.footer-stripe{position:absolute;left:0;top:1064px;width:100%;height:14px;background:var(--red)}
.footer{position:absolute;left:0;top:1078px;width:100%;height:122px;background:var(--blue);color:var(--white)}
.phone-icon{position:absolute;left:27px;top:15px;width:46px;height:90px}
.call-label{position:absolute;left:80px;top:6px;font-weight:300;font-size:38px;line-height:40px;letter-spacing:-.5px}
.call-number{position:absolute;left:78px;top:42px;font-weight:800;font-size:62px;line-height:70px;letter-spacing:-1px}
.contact-row{position:absolute;left:678px;display:flex;align-items:flex-start;gap:14px}
.contact-row .glyph{width:32px;height:32px;border-radius:50%;background:var(--white);display:flex;align-items:center;justify-content:center;flex:none}
.contact-row p{font-size:20px;line-height:24px;letter-spacing:2.2px;white-space:nowrap}
.row-address{top:14px}
.row-web{top:73px}
.row-web p{line-height:32px}
</style>
</head>
<body>
<main class="sheet">

  <header class="brand">
    <span class="brand-dot"></span>
    <span class="brand-name">Coolcrest Air</span>
  </header>

  <div class="intro-band"></div>
  <svg class="title-banner" viewBox="0 0 926 100" aria-hidden="true">
    <defs>
      <linearGradient id="bannerGrad" x1="0" x2="1">
        <stop offset="0" stop-color="#1f6aa8"/><stop offset=".5" stop-color="#3a8fd0"/><stop offset="1" stop-color="#1f6aa8"/>
      </linearGradient>
    </defs>
    <polygon points="26,0 900,0 926,50 900,100 26,100 0,50" fill="url(#bannerGrad)"/>
  </svg>
  <div class="title-banner"><h1>4 BENEFITS OF HVAC UV LIGHTS FOR YOUR SYSTEM</h1></div>

  <p class="intro-text">Ultraviolet (UV) devices offer numerous benefits when added to your home's heating and cooling system including keeping those cold and flu germs at bay. If you're concerned about boss indoor air quality affects your family's health, consider these four reasons to add UV lighting to your HVAC system.</p>

  <div class="benefits-badge">
    <svg width="324" height="72" viewBox="0 0 324 72" aria-hidden="true">
      <polygon points="0,37 324,37 316,72 8,72" fill="#c73a42"/>
      <polygon points="16,0 304,0 310,30 304,61 16,61 10,30" fill="url(#bannerGrad)"/>
    </svg>
    <span>4 BENEFITS</span>
  </div>

  <div class="timeline"></div>
  <div class="step bg-blue" style="left:59px">1</div>
  <div class="step bg-navy" style="left:312px">2</div>
  <div class="step bg-red" style="left:568px">3</div>
  <div class="step bg-crimson" style="left:821px">4</div>
  <div class="connector bg-blue" style="left:78px"></div>
  <div class="connector bg-navy" style="left:331px"></div>
  <div class="connector bg-red" style="left:587px"></div>
  <div class="connector bg-crimson" style="left:840px"></div>

  <article class="card" style="left:40px">
    <svg class="card-tab" viewBox="0 0 154 84" aria-hidden="true"><polygon points="0,0 96,0 153,75 0,75" fill="#2f86c6"/><polygon points="0,75 13,75 13,84" fill="#1f5f93"/></svg>
    <div class="card-num is-blue"><span>1</span></div>
    <div class="card-inner">
      <span class="card-icon bg-blue" role="img" aria-label="Fan with airflow icon"></span>
      <h2 class="is-blue">Improved Airflow</h2>
      <ul>
        <li><svg viewBox="0 0 10 10"><circle cx="5" cy="5" r="5" fill="#2f86c6"/><path d="M2.7 5.2l1.5 1.5 3-3" stroke="#fff" stroke-width="1.3" fill="none"/></svg>UV lighting works to prevent microbial buildup on air filters, cooling coils, drain pans, and duct surfaces. By eliminating contaminant build-up inside your HVAC system, heat exchange and airflow are both dramatically improved.</li>
        <li><svg viewBox="0 0 10 10"><circle cx="5" cy="5" r="5" fill="#2f86c6"/><path d="M2.7 5.2l1.5 1.5 3-3" stroke="#fff" stroke-width="1.3" fill="none"/></svg>The major benefits include reducing your home's energy use, improving indoor air quality, and reducing overall maintenance costs for your HVAC system.</li>
      </ul>
    </div>
    <div class="card-foot bg-blue"></div>
  </article>

  <article class="card" style="left:292px">
    <svg class="card-tab" viewBox="0 0 154 84" aria-hidden="true"><polygon points="0,0 96,0 153,75 0,75" fill="#134b7f"/><polygon points="0,75 13,75 13,84" fill="#0b3357"/></svg>
    <div class="card-inner">
      <span class="card-icon bg-navy" role="img" aria-label="Power plug icon"></span>
      <h2 class="is-navy">Inproved Energy Efficiency</h2>
      <ul>
        <li><svg viewBox="0 0 10 10"><circle cx="5" cy="5" r="5" fill="#134b7f"/><path d="M2.7 5.2l1.5 1.5 3-3" stroke="#fff" stroke-width="1.3" fill="none"/></svg>Adding a UV device to your existing HVAC system can reduce your home's overall energy consumption by up to 35%.</li>
        <li><svg viewBox="0 0 10 10"><circle cx="5" cy="5" r="5" fill="#134b7f"/><path d="M2.7 5.2l1.5 1.5 3-3" stroke="#fff" stroke-width="1.3" fill="none"/></svg>UV restores the HVAC system's performance to optimal levels, reducing its power consumption and helping it work like new.</li>
      </ul>
    </div>
    <div class="card-foot bg-navy"></div>
  </article>

  <article class="card" style="left:547px">
    <svg class="card-tab" viewBox="0 0 154 84" aria-hidden="true"><polygon points="0,0 96,0 153,75 0,75" fill="#c73a42"/><polygon points="0,75 13,75 13,84" fill="#8e232a"/></svg>
    <div class="card-num is-red"><span>3</span></div>
    <div class="card-inner">
      <span class="card-icon square bg-red" role="img" aria-label="Money saving icon"></span>
      <h2 class="is-red" style="margin-top:6px">Cost-Effective Investment</h2>
      <ul style="margin-top:8px">
        <li><svg viewBox="0 0 10 10"><circle cx="5" cy="5" r="5" fill="#c73a42"/><path d="M2.7 5.2l1.5 1.5 3-3" stroke="#fff" stroke-width="1.3" fill="none"/></svg>When you add a UV lighting device to the HVAC system, you're helping the system keep itself clean, which is why UV installations are so cost-effective when you consider all of the health-related and money-saving benefits.</li>
        <li><svg viewBox="0 0 10 10"><circle cx="5" cy="5" r="5" fill="#c73a42"/><path d="M2.7 5.2l1.5 1.5 3-3" stroke="#fff" stroke-width="1.3" fill="none"/></svg>UV lighning in your HVAC system can also boost your home's value and make it more attractive to potential buyers</li>
      </ul>
    </div>
    <div class="card-foot bg-red"></div>
  </article>

  <article class="card" style="left:801px">
    <svg class="card-tab" viewBox="0 0 154 84" aria-hidden="true"><polygon points="0,0 96,0 153,75 0,75" fill="#a11f26"/><polygon points="0,75 13,75 13,84" fill="#6e1218"/></svg>
    <div class="card-num is-crimson"><span>4</span></div>
    <div class="card-inner">
      <span class="card-icon bg-crimson" style="width:58px" role="img" aria-label="Heart held by hands with medical cross icon"></span>
      <h2 class="is-crimson">Disease Prevention</h2>
      <ul>
        <li><svg viewBox="0 0 10 10"><circle cx="5" cy="5" r="5" fill="#a11f26"/><path d="M2.7 5.2l1.5 1.5 3-3" stroke="#fff" stroke-width="1.3" fill="none"/></svg>The HVAC system circulates the air in your home, which means that it also circulate airborne bacteria and viruses.</li>
        <li><svg viewBox="0 0 10 10"><circle cx="5" cy="5" r="5" fill="#a11f26"/><path d="M2.7 5.2l1.5 1.5 3-3" stroke="#fff" stroke-width="1.3" fill="none"/></svg>The UV lighting used in HVAC systems prevents the buildup of organic material on e system's interior mechanics, killing pathogens and other microorganisms that would normally thrive in an HVAC system</li>
      </ul>
    </div>
    <div class="card-foot bg-crimson"></div>
  </article>

  <p class="closing">Whether you're just beginning to consider UV technology or you've already decided to go ahead with the installation, call Coolcrest Air to get started.</p>

  <div class="footer-stripe"></div>
  <footer class="footer">
    <svg class="phone-icon" viewBox="0 0 46 90" aria-hidden="true">
      <rect x="2" y="2" width="42" height="86" rx="6" fill="none" stroke="#fff" stroke-width="3.5"/>
      <line x1="2" y1="12" x2="44" y2="12" stroke="#fff" stroke-width="2.5"/>
      <line x1="2" y1="76" x2="44" y2="76" stroke="#fff" stroke-width="2.5"/>
      <rect x="17" y="80" width="12" height="3" rx="1.5" fill="#fff"/>
      <circle cx="9" cy="7" r="1.3" fill="#fff"/><rect x="16" y="6" width="14" height="2" rx="1" fill="#fff"/>
    </svg>
    <div class="call-label">CALL US ON</div>
    <div class="call-number">555 014-2270</div>

    <div class="contact-row row-address">
      <span class="glyph"><svg width="14" height="19" viewBox="0 0 14 19" aria-hidden="true"><path d="M7 0C3.1 0 0 3 0 6.9 0 12 7 19 7 19s7-7 7-12.1C14 3 10.9 0 7 0z" fill="#2f86c6"/><circle cx="7" cy="7" r="2.6" fill="#fff"/></svg></span>
      <p>1480 Lomas Ave,Tolan,<br>Arizona 86000</p>
    </div>
    <div class="contact-row row-web">
      <span class="glyph"><svg width="22" height="22" viewBox="0 0 22 22" aria-hidden="true" fill="none" stroke="#2f86c6" stroke-width="1.5"><circle cx="11" cy="11" r="9.5"/><ellipse cx="11" cy="11" rx="4.5" ry="9.5"/><line x1="1.5" y1="11" x2="20.5" y2="11"/><line x1="3" y1="6" x2="19" y2="6"/><line x1="3" y1="16" x2="19" y2="16"/><line x1="11" y1="1.5" x2="11" y2="20.5"/></svg></span>
      <p>www.coolcrestair.com</p>
    </div>
  </footer>

</main>
</body>
</html>
```